VFX Company Business Card Design Project

The Ember Vale is a decentralized Visual Effects Studio servicing the television and feature film industries.
Project Brief:
Take our logo that was previously designed on Pixel Harbor and make a double sided business card.
Requirements:
- Card MUST be double sided.
- Front of card MUST have the yellow part of our logo against the dark grey background.
- Back of card is completely up to the designer.
- Back of card must include the complete company logo.
Please follow these File Preparation guidelines:
http://printmoor.example/infopage?file=filetype_en&s=PrintMoor_new&lang=en
Industry/Entity Type
Business
Look and feel
Each slider illustrates characteristics of the customer's brand and the style your logo design should communicate.

```html
<!DOCTYPE html>
<html lang="en">
<head>
<meta charset="utf-8">
<title>The Ember Vale – Business Card</title>
<link rel="stylesheet" href="https://fonts.googleapis.com/css2?family=Questrial&display=swap">
<style>
  :root {
    --card-dark: #262626;
    --brand-yellow: #f2be1e;
    --brand-grey: #8d9396;
    --ink: #1c1c1c;
    --ink-soft: #6b6e70;
    --paper: #ffffff;
  }
  * { margin: 0; padding: 0; box-sizing: border-box; }
  html, body { width: 876px; height: 1200px; overflow: hidden; background: var(--paper); }
  body { position: relative; font-family: "Questrial", "Century Gothic", sans-serif; }

  .card-front {
    position: absolute; left: 28px; top: 34px; width: 818px; height: 528px;
    background: var(--card-dark);
  }
  .front-logo {
    position: absolute; left: 140px; top: 255px;
    display: flex; align-items: center; gap: 24px;
  }
  .front-logo .mark { width: 64px; height: 64px; border-radius: 50%; background: var(--brand-yellow); }
  .front-logo .name {
    font-size: 50px; letter-spacing: 1px; color: var(--brand-grey); line-height: 1; white-space: nowrap;
  }
  .front-tagline {
    position: absolute; left: 368px; top: 322px;
    font-size: 17px; letter-spacing: 8px; color: var(--brand-grey);
  }

  .card-back {
    position: absolute; left: 28px; top: 627px; width: 818px; height: 529px;
    background: var(--paper);
  }
  .back-logo {
    position: absolute; left: 28px; top: 46px;
    display: flex; align-items: center; gap: 10px;
  }
  .back-logo .mark { width: 24px; height: 24px; border-radius: 50%; background: var(--brand-yellow); }
  .back-logo .name { font-size: 22px; color: var(--brand-grey); line-height: 1; }

  .identity { position: absolute; right: 20px; top: 140px; text-align: right; }
  .identity .company { font-size: 64px; line-height: 1; letter-spacing: 1px; }
  .identity .company .first { color: var(--ink-soft); }
  .identity .company .second { color: var(--ink); }
  .identity .tagline { font-size: 38px; color: var(--brand-yellow); margin-top: 4px; line-height: 1.1; }

  .contact {
    position: absolute; right: 20px; top: 305px; text-align: right;
    font-size: 32px; line-height: 40px; color: var(--ink); list-style: none;
  }
  .website {
    position: absolute; right: 20px; top: 486px;
    font-size: 31px; color: var(--ink-soft); letter-spacing: 0.5px;
  }
</style>
</head>
<body>
  <section class="card-front">
    <div class="front-logo">
      <span class="mark"></span>
      <span class="name">THE EMBER VALE</span>
    </div>
    <p class="front-tagline">VIRTUAL STUDIO</p>
  </section>

  <section class="card-back">
    <div class="back-logo">
      <span class="mark"></span>
      <span class="name">EMBER VALE</span>
    </div>
    <div class="identity">
      <h1 class="company"><span class="first">EMBER</span> <span class="second">VALE</span></h1>
      <p class="tagline">Virtual Studio</p>
    </div>
    <ul class="contact">
      <li>T: 01632 4907315</li>
      <li>M: 07700 900482</li>
      <li>E: you@embervale.co.uk</li>
    </ul>
    <p class="website">www.embervale.co.uk</p>
  </section>
</body>
</html>
```